Business Card Re-Design for a Lighting Designer

I would like my business card re-designed. It is currently high gloss and they scratch too easily. I don not think the current design lends itself well to a matte finish. I have included the current design for reference along with our company logo.
Check out our website for current branding.
http://www.brambleorchidstudio.example

Updates
Some of the top contenders are muslim and it is a holiday for them. I do not want to discriminate and would expect the same courtesy for holidays we celebrate.
Target Market(s)
Interior Designers, Architects
Contact Information for Business Card
Logo - Name, Title, Address, Telephone Number and Extension, Email
Font styles to use
Requirements
Must have
- All the information listed on the current business card. If you use Red, it needs to be the red from our logo.
Nice to have
- Vertical and Horizontal Designs will be entertained.
Should not have
- Requirements for a glossy finish...should not look too corporate since we are a design firm.

```html
<!DOCTYPE html>
<html lang="en">
<head>
<meta charset="utf-8">
<title>Bramble Orchid Studio — Business Card</title>
<link rel="stylesheet" href="https://fonts.googleapis.com/css2?family=Noto+Sans:wght@400;700&display=swap">
<style>
  :root {
    --brand-red: #9b0b0b;
    --card-cream: #faf3df;
    --photo-red-light: #b82a2a;
    --photo-red-dark: #8e1414;
    --white: #ffffff;
    --page: #ffffff;
  }
  * { margin: 0; padding: 0; box-sizing: border-box; }
  html, body {
    width: 1200px; height: 920px; overflow: hidden;
    background: var(--page);
    font-family: "Noto Sans", Arial, sans-serif;
  }
  .canvas { position: relative; width: 1200px; height: 920px; }
  .card {
    position: absolute; top: 38px; width: 514px; height: 841px;
    box-shadow: 0 6px 22px rgba(0,0,0,0.22);
  }
  .card--front { left: 39px; background: var(--card-cream); color: var(--brand-red); }
  .card--back { left: 646px; color: var(--white); overflow: hidden; }

  /* wordmark */
  .wordmark { position: absolute; display: flex; flex-direction: column; }
  .wordmark__row { display: flex; align-items: flex-start; gap: 8px; }
  .wordmark__square { flex: none; }
  .wordmark__name { font-weight: 400; line-height: 1.05; text-transform: uppercase; }
  .wordmark__rule { height: 1px; }
  .wordmark__tagline { font-weight: 400; text-transform: uppercase; letter-spacing: 0.06em; }

  .card--front .wordmark { left: 364px; top: 33px; width: 120px; }
  .card--front .wordmark__square { width: 22px; height: 22px; background: var(--brand-red); }
  .card--front .wordmark__name { font-size: 17px; color: var(--brand-red); }
  .card--front .wordmark__rule { background: var(--brand-red); margin-top: 7px; }
  .card--front .wordmark__tagline { font-size: 7px; margin-top: 4px; color: var(--brand-red); }

  .person { position: absolute; left: 0; width: 514px; top: 410px; text-align: center; }
  .person__name { font-size: 40px; font-weight: 700; line-height: 1; letter-spacing: 0.005em; }
  .person__title { font-size: 22px; font-weight: 400; letter-spacing: 0.55em; margin-top: 4px; padding-left: 0.55em; line-height: 1.1; }

  .contact {
    position: absolute; left: 32px; bottom: 28px;
    list-style: none; font-size: 16px; line-height: 19px;
  }
  .contact__item { display: flex; align-items: flex-start; gap: 9px; margin-bottom: 10px; }
  .contact__item:last-child { margin-bottom: 0; }
  .contact__icon { width: 18px; height: 18px; flex: none; margin-top: 1px; }
  .contact__item--address .contact__icon { margin-top: 9px; }

  .card__photo {
    position: absolute; inset: 0;
    background: linear-gradient(160deg, var(--photo-red-light) 0%, #a31f1f 45%, var(--photo-red-dark) 100%);
  }
  .card--back .wordmark { left: 161px; top: 297px; width: 240px; }
  .card--back .wordmark__square { width: 46px; height: 46px; background: var(--white); }
  .card--back .wordmark__name { font-size: 34px; color: var(--white); }
  .card--back .wordmark__rule { background: var(--white); margin-top: 14px; }
  .card--back .wordmark__tagline { font-size: 13px; margin-top: 9px; color: var(--white); }
  .card__url { position: absolute; bottom: 28px; left: 0; width: 514px; text-align: center; font-size: 16px; line-height: 19px; }
</style>
</head>
<body>
<div class="canvas">

  <section class="card card--front" aria-label="Card front">
    <div class="wordmark">
      <div class="wordmark__row">
        <span class="wordmark__square"></span>
        <span class="wordmark__name">Bramble<br>Orchid<br>Studio</span>
      </div>
      <div class="wordmark__rule"></div>
      <div class="wordmark__tagline">Lighting for Architecture</div>
    </div>

    <div class="person">
      <h1 class="person__name">MARLOW FENWICK</h1>
      <p class="person__title">PRINCIPAL</p>
    </div>

    <ul class="contact">
      <li class="contact__item contact__item--address">
        <svg class="contact__icon" viewBox="0 0 18 18" aria-hidden="true"><rect x="2" y="2" width="2" height="15" fill="#9b0b0b"/><path d="M4 2 L16 6.5 L4 11 Z" fill="#9b0b0b"/></svg>
        <span>412 Larkspur Row, Suite 210<br>Fairhaven, Georgia 30999 USA</span>
      </li>
      <li class="contact__item">
        <svg class="contact__icon" viewBox="0 0 18 18" aria-hidden="true"><rect x="1" y="4" width="16" height="11" fill="#9b0b0b"/><path d="M1.5 4.5 L9 10.5 L16.5 4.5 M1.5 14.5 L7 9 M16.5 14.5 L11 9" stroke="#faf3df" stroke-width="1.3" fill="none"/></svg>
        <span>marlow@brambleorchidstudio.example</span>
      </li>
      <li class="contact__item">
        <svg class="contact__icon" viewBox="0 0 18 18" aria-hidden="true"><path d="M4 1.5 L7 5 L5.5 7 Q7.5 10.5 11 12.5 L13 11 L16.5 14 L14.5 16.5 Q8 16 4 11 Q1 7 1.5 3.5 Z" fill="#9b0b0b"/></svg>
        <span>555.014.2280 x1</span>
      </li>
      <li class="contact__item">
        <svg class="contact__icon" viewBox="0 0 18 18" aria-hidden="true"><g fill="none" stroke="#9b0b0b" stroke-width="1.2"><circle cx="9" cy="9" r="7.5"/><ellipse cx="9" cy="9" rx="3.3" ry="7.5"/><path d="M1.5 9 H16.5 M3 5 H15 M3 13 H15"/></g></svg>
        <span>www.brambleorchidstudio.example</span>
      </li>
    </ul>
  </section>

  <section class="card card--back" aria-label="Card back">
    <div class="card__photo" role="img" aria-label="Red-toned photograph of a lit architectural atrium with steel roof framing"></div>
    <div class="wordmark">
      <div class="wordmark__row">
        <span class="wordmark__square"></span>
        <span class="wordmark__name">Bramble<br>Orchid<br>Studio</span>
      </div>
      <div class="wordmark__rule"></div>
      <div class="wordmark__tagline">Lighting for Architecture</div>
    </div>
    <p class="card__url">www.brambleorchidstudio.example</p>
  </section>

</div>
</body>
</html>
```